Redesign of Plastic Surgeon Website to fully responsive / modern feel

Hi

Our current website is out of date www.harbourlinecosmetic.org

We want a fresh / modern looking design
Needs to be fully responsive design that works extremely well on ipad and mobile device

Would like design for both full screen website and mobile

Have listed a few websites of other plastic surgeons we like
http://www.reformclinicdaily.com/
http://www.peterholtbymd.com/
http://www.corvanbeauty.com/
http://www.tidewellcontouring.com/

Menu needs to include
1. About Us
2. Procedures (see current website for example)
3. News
4. Patient Resources
5. Contact Us

We are flexible with colours / images / layout

I have uploaded a document that has some content - the face pages content is completed only

some of the procedures can have content upwards of 4000 words - total website can be large with over 40,000 words
Updates

Target Market(s)

Mainly women 20-60 85% of practice
Some men 15%

Industry/Entity Type

Plastic Surgery

Number of Pages Required

5+ page

Requirements
Must have
• We need designs for
• Homepage
• Internal pages
• 1. Landing pages for breast / body / face / non surgical main pages
• 2. Procedure pages for individual pages under each section - eg breast augmentation
• 3. About us pages - like meet the doctor, our staff, clinics
• 4. Contact page
• 5. Blog / News page
Nice to have
• See our list of websites for examples of designs we like
• Like full screen design with nice hero image
• Needs to have good to call to action messages on home page like
• Specials, procedure of the month, etc

```html
<!DOCTYPE html>
<html lang="en">
<head>
<meta charset="utf-8">
<title>Harbourline Cosmetic</title>
<link href="https://fonts.googleapis.com/css2?family=Source+Sans+3:wght@300;400;600;700;900&display=swap" rel="stylesheet">
<style>
:root{
  --gold:#e8b730;
  --gold-dark:#b8892d;
  --ink:#1f1c19;
  --charcoal:#2f2c29;
  --footer:#46413b;
  --band:#e4e4e4;
  --text:#5a544d;
  --beige-a:#efe5d3;
  --beige-b:#dccab0;
  --white:#ffffff;
}
*{margin:0;padding:0;box-sizing:border-box}
html,body{width:916px;height:1200px;overflow:hidden}
body{position:relative;font-family:"Source Sans 3",sans-serif;background:var(--white);color:var(--text)}
.abs{position:absolute}
.header{left:0;top:0;width:916px;height:70px;background:var(--white)}
.brand{left:72px;top:0;width:92px;height:110px;background:var(--charcoal);z-index:3;display:flex;flex-direction:column;justify-content:center;align-items:center;color:#d8d2c6;font-size:12px;font-weight:400;letter-spacing:1px;text-align:center;line-height:1.35}
.call{left:678px;top:7px;height:27px;display:flex;font-size:13px;font-weight:600}
.call-label{background:var(--gold);color:var(--white);padding:0 10px;display:flex;align-items:center}
.call-number{background:var(--charcoal);color:var(--white);padding:0 10px;display:flex;align-items:center;font-weight:700}
.nav{left:317px;top:46px;display:flex;gap:0;font-size:12.5px;color:var(--ink)}
.nav span{margin-right:40px}
.nav span:last-child{margin-right:0}
.hero{left:2px;top:70px;width:914px;height:335px;background:linear-gradient(180deg,var(--beige-a),var(--beige-b))}
.hero-photo{left:476px;top:70px;width:387px;height:335px;background:radial-gradient(ellipse at 55% 40%,#d9b39a 0%,#8a6552 35%,#2c2019 70%,#dccab0 100%)}
.side-tab{left:884px;top:160px;width:32px;height:100px;background:var(--charcoal);color:var(--white);font-size:13px;font-weight:600;display:flex;align-items:center;justify-content:center}
.side-tab span{transform:rotate(-90deg);white-space:nowrap}
.hero-intro{left:72px;top:162px;font-size:16px;font-weight:300;color:var(--ink)}
.hero-title{left:72px;top:184px;font-size:29px;font-weight:900;color:var(--ink);letter-spacing:.3px}
.hero-big{left:70px;top:212px;font-size:58px;font-weight:900;color:var(--white);letter-spacing:1px;line-height:1}
.btn{background:var(--gold);color:var(--white);font-size:12px;font-weight:700;display:flex;align-items:center;justify-content:center;border-radius:2px;letter-spacing:.3px}
.hero-btn{left:74px;top:288px;width:110px;height:33px}
.dots{left:74px;top:335px;display:flex;gap:7px}
.dots i{width:7px;height:7px;background:#d4c1a4}
.dots i:first-child{background:var(--gold)}
.band{left:2px;top:405px;width:914px;height:169px;background:var(--band)}
.card{top:428px;width:172px;height:127px}
.card-img{height:99px}
.card-label{height:28px;background:var(--gold);color:var(--ink);font-size:14px;display:flex;align-items:center;justify-content:center}
.badge{left:6px;top:6px;width:53px;height:53px;border-radius:50%;background:var(--gold);color:var(--ink);font-size:17px;line-height:1;display:flex;flex-direction:column;align-items:center;justify-content:center}
.badge small{font-size:11px}
.welcome-img{left:72px;top:645px;width:271px;height:180px;background:linear-gradient(135deg,#f3ece6,#dccfc6 60%,#c9c0ba)}
.welcome-h{left:370px;top:603px;font-size:29px;font-weight:300;color:var(--gold-dark)}
.rule{left:370px;top:645px;width:474px;height:1px;background:#cfc8be}
.rule-accent{left:370px;top:644px;width:29px;height:3px;background:var(--gold-dark)}
.welcome-text{left:370px;top:660px;width:476px;font-size:12px;line-height:18.5px;font-weight:400}
.welcome-text p{margin-bottom:18.5px}
.welcome-btn{left:370px;top:834px;width:110px;height:33px}
.partners{left:2px;top:893px;width:914px;height:82px;background:var(--charcoal)}
.partner{top:910px;height:48px;background:#5b5650;opacity:.8}
.footer{left:2px;top:975px;width:914px;height:225px;background:var(--footer)}
.col{top:1002px;font-size:12px;line-height:20px;color:#e4dfd6}
.col h4{color:var(--gold);font-weight:700;font-size:12.5px;margin-bottom:1px}
.clinic{line-height:16.5px}
</style>
</head>
<body>
<div class="abs header"></div>
<div class="abs brand">HARBOUR<br>LINE<br>COSMETIC</div>
<div class="abs call"><div class="call-label">Call Now</div><div class="call-number">02 5550 1942</div></div>
<div class="abs nav"><span>Home</span><span>About us</span><span>Procedures</span><span>Patient Resources</span><span>News/Blog</span><span>Contact us</span></div>

<div class="abs hero"></div>
<div class="abs hero-photo" role="img" aria-label="Portrait of a smiling woman with long dark hair"></div>
<div class="abs side-tab"><span>Contact us</span></div>
<div class="abs hero-intro">At the Harbourline Cosmetic Clinic</div>
<div class="abs hero-title">YOUR FUTURE LOOKS</div>
<div class="abs hero-big">BEAUTIFUL</div>
<div class="abs btn hero-btn">LEARN MORE</div>
<div class="abs dots"><i></i><i></i><i></i><i></i><i></i></div>

<div class="abs band"></div>
<div class="abs card" style="left:73px">
  <div class="card-img" role="img" aria-label="Consultation between surgeon and patient" style="background:linear-gradient(135deg,#efe7dc,#b9a58a)"></div>
  <div class="card-label">Procedure of the Month</div>
</div>
<div class="abs card" style="left:271px">
  <div class="card-img" role="img" aria-label="Woman resting her chin on her hands" style="position:relative;background:linear-gradient(90deg,#ffffff,#f1e6db)"><div class="abs badge">25%<small>OFF</small></div></div>
  <div class="card-label">Specials</div>
</div>
<div class="abs card" style="left:472px">
  <div class="card-img" role="img" aria-label="Portrait of the surgeon" style="background:linear-gradient(135deg,#14202c,#24404f 60%,#0f1a24)"></div>
  <div class="card-label">Meet Mr. Halden</div>
</div>
<div class="abs card" style="left:673px">
  <div class="card-img" role="img" aria-label="Body contouring result on a woman's waist" style="background:linear-gradient(180deg,#f7f3f0,#e8d6cc)"></div>
  <div class="card-label">Fat Freezing / Contouring</div>
</div>

<div class="abs welcome-img" role="img" aria-label="Patient receiving a facial skin treatment"></div>
<div class="abs welcome-h">Welcome</div>
<div class="abs rule"></div>
<div class="abs rule-accent"></div>
<div class="abs welcome-text">
  <p>You can expect beautiful results at the Harbourline Cosmetic Clinic. Offering unparalleled expertise in face, breast and body enhancement, including facelifts, breast augmentation / lift / reduction or tummy tucks, we offer total care at every step of your transformative journey.</p>
  <p>Dr Halden is one of Australia’s most eminent specialists in plastic and cosmetic surgery, and is supported by our highly qualified, professional team. As Sydney’s premier plastic surgery clinic, we use only the most revolutionary techniques to minimise scarring to help you look better, feel better and enjoy a beautiful new you.</p>
</div>
<div class="abs btn welcome-btn">LEARN MORE</div>

<div class="abs partners"></div>
<div class="abs partner" style="left:76px;width:57px;border-radius:50%"></div>
<div class="abs partner" style="left:166px;width:64px"></div>
<div class="abs partner" style="left:268px;width:98px"></div>
<div class="abs partner" style="left:390px;width:56px"></div>
<div class="abs partner" style="left:477px;width:135px"></div>
<div class="abs partner" style="left:644px;width:100px"></div>
<div class="abs partner" style="left:781px;width:64px"></div>

<div class="abs footer"></div>
<div class="abs col" style="left:72px"><h4>Face</h4>Facelift<br>Eyelid Surgery<br>Brow Lift Surgery<br>Rhinoplasty Surgery<br>Otoplasty Surgery<br>Laser Resurfacing<br>Chin Enlargement</div>
<div class="abs col" style="left:257px"><h4>Body</h4>Tummy Tuck<br>Liposuction<br>Brachioplasty</div>
<div class="abs col" style="left:445px"><h4>Breast</h4>Breast Augmentation<br>Breast Reduction<br>Breast Lift<br>Breast Reconstruction<br>Gynecomastia</div>
<div class="abs col" style="left:643px"><h4>Our Clinics</h4><div class="clinic">Northcove<br>127 Bayview Rd, Suite 12<br>Northcove, NSW 2099<br><br>Westbury<br>Level 1<br>46 Marlow Street<br>2040</div></div>
</body>
</html>
```